MAPLE & FINCH

LAUNDRY & DRY CLEAN SERVICE

Low design quality

Colors
acd036
0293ce

Requirements
Must have
• the maple & finch logo must on both car sides + rear & front
• ** Sample car wrap (attached)
Nice to have
• attractive color

```html
<!DOCTYPE html>
<html lang="en">
<head>
<meta charset="utf-8">
<title>Maple &amp; Finch – Van Wrap Side Panel</title>
<link rel="stylesheet" href="https://fonts.googleapis.com/css2?family=Nunito:wght@700;800;900&family=Roboto+Condensed:wght@800&family=Cairo:wght@700&display=swap">
<style>
  :root {
    --brand-green: #6cbd45;
    --brand-green-dark: #2f6a1f;
    --brand-blue: #00a9ec;
    --brand-blue-deep: #1a8fd6;
    --wrap-white: #ffffff;
    --wrap-mist: #dfe6dd;
    --ink: #111111;
    --page-bg: #eeeeee;
    --icon-tint: #8fcf6a;
  }
  * { margin: 0; padding: 0; box-sizing: border-box; }
  html, body {
    width: 1200px; height: 799px; overflow: hidden;
    background: var(--page-bg);
  }
  .wrap-panel {
    position: relative;
    width: 1200px; height: 799px;
    font-family: "Nunito", sans-serif;
  }
  .wrap-graphic { position: absolute; inset: 0; }
  .site-url {
    position: absolute; left: 255px; top: 215px;
    font-weight: 900; font-size: 15px; color: var(--ink);
    letter-spacing: 0.2px;
  }
  .brand-mark {
    position: absolute; left: 130px; top: 240px;
    width: 90px; height: 90px; border-radius: 50%;
    background: var(--brand-blue-deep);
  }
  .brand-name {
    position: absolute; left: 236px; top: 228px;
    font-weight: 900; font-size: 46px; line-height: 1;
    color: var(--brand-blue-deep); letter-spacing: -0.5px;
    white-space: nowrap;
  }
  .brand-tagline {
    position: absolute; left: 238px; top: 272px;
    font-weight: 800; font-size: 15.5px;
    color: var(--brand-blue-deep); white-space: nowrap;
  }
  .brand-tagline .amp { color: var(--brand-green); }
  .arabic-line {
    position: absolute; left: 238px; top: 290px; width: 262px;
    display: flex; align-items: center; gap: 8px;
  }
  .arabic-line .rule { flex: 1; height: 2px; background: var(--brand-green); }
  .arabic-line .arabic-name {
    font-family: "Cairo", sans-serif; font-weight: 700;
    font-size: 17px; color: var(--brand-blue-deep); line-height: 1.2;
  }
  .phone-number {
    position: absolute; left: 252px; top: 312px;
    font-family: "Roboto Condensed", sans-serif; font-weight: 800;
    font-size: 46px; color: var(--ink); letter-spacing: 0.5px;
  }
  .social-dot {
    position: absolute; top: 392px; width: 48px; height: 48px;
    border-radius: 50%; background: var(--icon-tint);
  }
  .social-dot.first { left: 120px; }
  .social-dot.second { left: 175px; }
  .social-handle {
    position: absolute; left: 238px; top: 428px;
    font-weight: 700; font-size: 23px; color: var(--ink);
  }
</style>
</head>
<body>
<main class="wrap-panel">
  <svg class="wrap-graphic" width="1200" height="799" viewBox="0 0 1200 799" aria-hidden="true">
    <defs>
      <linearGradient id="wrap-fade" x1="0" y1="0" x2="0.35" y2="1">
        <stop offset="0" stop-color="var(--wrap-white)"/>
        <stop offset="0.45" stop-color="var(--wrap-mist)"/>
        <stop offset="1" stop-color="var(--brand-green-dark)"/>
      </linearGradient>
      <clipPath id="panel-clip">
        <rect x="100" y="150" width="1000" height="440" rx="40"/>
      </clipPath>
    </defs>
    <g clip-path="url(#panel-clip)">
      <rect x="100" y="150" width="1000" height="440" fill="url(#wrap-fade)"/>
      <!-- upper blue sweep -->
      <path d="M470 150 L500 150 C540 230 600 300 680 350 L1100 520 L1100 545 L660 365 C580 320 515 240 470 150 Z" fill="var(--brand-blue)"/>
      <!-- lower green field -->
      <path d="M100 380 C300 390 500 430 700 480 L1100 600 L100 600 Z" fill="var(--brand-green)"/>
      <!-- main blue band -->
      <path d="M100 358 C320 365 520 410 720 470 L900 530 L900 545 L700 482 C500 425 300 385 100 378 Z" fill="var(--brand-blue)"/>
      <!-- lower right blue accent -->
      <path d="M760 515 L1100 560 L1100 600 L880 600 Z" fill="var(--brand-blue)"/>
    </g>
  </svg>

  <p class="site-url">www.maple-finch-laundry.com</p>
  <div class="brand-mark"></div>
  <h1 class="brand-name">MAPLE &amp; FINCH</h1>
  <p class="brand-tagline">LAUNDRY <span class="amp">&amp;</span> DRY CLEAN SERVICE</p>
  <div class="arabic-line">
    <span class="rule"></span>
    <span class="arabic-name" lang="ar" dir="rtl">مغسلة مابل وفينش</span>
    <span class="rule"></span>
  </div>
  <p class="phone-number">555-014280</p>
  <span class="social-dot first"></span>
  <span class="social-dot second"></span>
  <p class="social-handle">maple-finch-laundry</p>
</main>
</body>
</html>
```